Business card for new consulting business - Brackenvale Enterprises Pty Ltd.

Consulting in the areas of Occupational Health, Safety and Community Relations in the resources (mining) industries. The consultant (me) will work both within Australia and overseas jurisdictions such as South East Asia, Africa , South America etc, often working with third world indigenous communities. The design should suggest a high level of social and environmental responsibility.

```html
<!DOCTYPE html>
<html lang="en">
<head>
<meta charset="utf-8">
<title>Brackenvale Enterprises – Business Card</title>
<link rel="stylesheet" href="https://fonts.googleapis.com/css2?family=Oswald:wght@400;500&family=Open+Sans:wght@400;600&display=swap">
<style>
  :root {
    --bg: #161616;
    --card: #232323;
    --card-edge: #2c2c2c;
    --green: #5cbf3a;
    --silver: #d4d4d4;
    --text: #bdbdbd;
    --muted: #8e8e8e;
    --rule: #4a4a4a;
  }
  * { margin: 0; padding: 0; box-sizing: border-box; }
  html, body { width: 1200px; height: 900px; overflow: hidden; background: var(--bg); }
  body { position: relative; font-family: "Open Sans", sans-serif; }

  .card {
    position: absolute;
    left: 250px;
    width: 700px;
    height: 400px;
    background: var(--card);
    border: 1px solid var(--card-edge);
    border-radius: 28px;
  }
  .card--back { top: 36px; }
  .card--front { top: 464px; }

  /* Back */
  .brand-mark {
    position: absolute;
    left: 0; right: 0; top: 150px;
    display: flex; align-items: center; justify-content: center; gap: 16px;
  }
  .brand-mark__dot { width: 18px; height: 18px; border-radius: 50%; background: var(--silver); }
  .brand-mark__name {
    font-family: "Oswald", sans-serif; font-weight: 500;
    font-size: 64px; letter-spacing: 1px; color: var(--silver);
  }
  .website {
    position: absolute; left: 0; right: 0; top: 300px;
    text-align: center; font-size: 15px; letter-spacing: 3px; color: var(--text);
  }

  /* Front */
  .company {
    position: absolute; right: 48px; top: 48px; text-align: right;
  }
  .company__row { display: flex; align-items: center; justify-content: flex-end; gap: 12px; }
  .company__dot { width: 14px; height: 14px; border-radius: 50%; background: var(--green); }
  .company__name {
    font-family: "Oswald", sans-serif; font-weight: 500;
    font-size: 30px; color: var(--silver); letter-spacing: .5px; text-transform: uppercase;
  }
  .company__suffix {
    font-family: "Oswald", sans-serif; font-weight: 500;
    font-size: 11px; color: var(--silver); letter-spacing: 1px; margin-top: 2px;
  }
  .rule { position: absolute; height: 1px; background: var(--rule); }
  .rule--top { right: 48px; top: 148px; width: 330px; }
  .rule--mid { left: 250px; right: 48px; top: 250px; }

  .person { position: absolute; left: 48px; top: 218px; }
  .person__name {
    font-family: "Oswald", sans-serif; font-weight: 500;
    font-size: 28px; color: var(--silver); text-transform: uppercase; line-height: 1;
  }
  .person__name .accent { color: var(--green); }
  .person__role { font-size: 15px; color: var(--muted); margin-top: 4px; }

  .contacts { position: absolute; left: 60px; top: 300px; list-style: none; }
  .contacts li { display: flex; align-items: center; gap: 10px; font-size: 16px; color: var(--text); line-height: 26px; }
  .contacts svg { width: 14px; height: 14px; fill: var(--green); }

  .address {
    position: absolute; right: 48px; top: 266px; text-align: right;
    font-size: 15px; color: var(--text); line-height: 22px;
  }
</style>
</head>
<body>
  <section class="card card--back" aria-label="Card back">
    <div class="brand-mark">
      <span class="brand-mark__dot"></span>
      <span class="brand-mark__name">Brackenvale</span>
    </div>
    <p class="website">www.brackenvale.net</p>
  </section>

  <section class="card card--front" aria-label="Card front">
    <div class="company">
      <div class="company__row">
        <span class="company__dot"></span>
        <span class="company__name">Brackenvale Enterprises</span>
      </div>
      <div class="company__suffix">PTY LTD</div>
    </div>
    <div class="rule rule--top"></div>

    <div class="person">
      <h1 class="person__name">Daniel <span class="accent">Harper</span></h1>
      <p class="person__role">Managing Director</p>
    </div>
    <div class="rule rule--mid"></div>

    <ul class="contacts">
      <li><svg viewBox="0 0 16 16" aria-hidden="true"><path d="M3 1h3l1.5 4-2 1.2a9 9 0 0 0 4.3 4.3L11 8.5l4 1.5v3a2 2 0 0 1-2 2A12 12 0 0 1 1 3a2 2 0 0 1 2-2z"/></svg>044-987 654 321</li>
      <li><svg viewBox="0 0 16 16" aria-hidden="true"><path d="M4.5 0h7A1.5 1.5 0 0 1 13 1.5v13a1.5 1.5 0 0 1-1.5 1.5h-7A1.5 1.5 0 0 1 3 14.5v-13A1.5 1.5 0 0 1 4.5 0zM5 2v10h6V2zm3 11a1 1 0 1 0 0 2 1 1 0 0 0 0-2z"/></svg>044-987 654 321</li>
      <li><svg viewBox="0 0 16 16" aria-hidden="true"><path d="M0 3h16v10H0zm1.5 1.2v.3L8 9l6.5-4.5v-.3z"/></svg>info@brackenvale.net</li>
    </ul>

    <address class="address" style="font-style: normal;">
      88, Ridgeway Street<br>
      Perth WA, 6000
    </address>
  </section>
</body>
</html>
```